Brochure Design Project for a Psychotherapy Private Practice.

I am a psychologist and I own my private practice. I need brochures to market to doctors and healthcare providers so that they understand the psychotherapy services that I deliver. I also want the brochures to be informative to potential patients. I have included a word document that details the services that I offer.
Target Market(s)
Referring healthcare providers (medical doctors, naturopaths, physician assistants, nurse practitioners) and patients who are seeking psychotherapy.
Industry/Entity Type
Healthcare
Colors
Designer to choose colors to be used in the design.

```html
<!DOCTYPE html>
<html lang="en">
<head>
<meta charset="utf-8">
<title>Harbor Point Psychological Services – Trifold Brochure</title>
<link rel="stylesheet" href="https://fonts.googleapis.com/css2?family=Open+Sans:ital,wght@0,400;0,600;0,700;1,400;1,600&family=Raleway:wght@300;400;600;700&display=swap">
<style>
:root{
  --bg:#3a3a3c;
  --paper:#ffffff;
  --ink:#3b4448;
  --teal-dark:#1e4550;
  --teal-mid:#3d7380;
  --teal-soft:#5d949e;
  --navy:#14303b;
  --accent:#2f8c9c;
  --sky:#5cc0de;
  --muted:#e7eef0;
}
*{box-sizing:border-box;margin:0;padding:0}
html,body{width:1200px;height:2267px;overflow:hidden;background:var(--bg)}
body{position:relative;font-family:"Open Sans",Arial,sans-serif;color:var(--ink)}
.spread{position:absolute;left:30px;width:1140px;height:881px;display:flex;box-shadow:0 14px 40px rgba(0,0,0,.45)}
.spread--outside{top:150px}
.spread--inside{top:1236px}
.panel{position:relative;width:380px;height:100%;overflow:hidden;background:var(--paper)}
.body-text{font-size:9.6px;line-height:1.5;margin-bottom:8px}
.heading-teal{font-family:"Open Sans",Arial,sans-serif;font-weight:700;color:var(--accent);font-size:12.5px;margin:6px 0 3px}
.heading-dark{font-weight:700;color:var(--ink);font-size:16px;margin:10px 0 2px}
.heading-sub{font-weight:700;color:var(--accent);font-size:12px;margin:4px 0 2px}

/* outside left */
.approach{padding:34px 26px}

/* outside middle */
.bio{background:var(--teal-dark);color:#dfe9ec;height:410px;padding:30px 26px}
.bio__title{font-weight:700;color:#fff;font-size:13px;margin-bottom:6px}
.bio .body-text{color:#d6e4e7}
.bio__portrait{float:right;width:96px;height:104px;margin:-18px 0 6px 10px;border:3px solid #fff;border-radius:10px;background:linear-gradient(160deg,#c9a58a,#7a5a48)}
.contact{background:linear-gradient(180deg,var(--teal-mid),var(--teal-soft));height:351px;padding:40px 26px 0;text-align:center;color:#eef5f6}
.contact__lead{font-family:"Raleway",sans-serif;font-weight:300;font-size:17px;margin-bottom:18px}
.contact__lines{font-size:13px;line-height:1.55;margin-bottom:18px}
.contact__phone{font-weight:700;font-size:19px;color:#fff;margin-bottom:26px}
.contact__email{font-weight:700;font-size:17px;color:#fff}
.map{height:120px;background:linear-gradient(135deg,#eef2f4 0%,#dfe7ea 55%,#8fd0e6 80%,#4fb4d8 100%)}

/* cover */
.cover__brand{height:150px;display:flex;align-items:center;gap:16px;padding:0 34px}
.brand-dot{width:46px;height:46px;border-radius:50%;background:var(--accent);flex:none}
.brand-name{font-family:"Raleway",sans-serif;font-weight:300;color:#3d6e78;font-size:24px;line-height:1.15}
.cover__photo{height:440px;background:radial-gradient(circle at 40% 35%,#f4d6a0 0%,#b98d55 18%,#3b3c3a 45%,#16191b 80%)}
.cover__tagline{height:291px;background:linear-gradient(180deg,var(--teal-mid),var(--teal-dark) 40%,var(--navy));padding:60px 34px;font-family:"Raleway",sans-serif;font-weight:300;color:var(--sky);font-size:32px;line-height:1.2}

/* inside left */
.focus{padding:30px 26px 0}
.focus__title{font-weight:700;font-size:15px;color:var(--ink);margin-bottom:6px}
.focus__intro{font-style:italic;font-weight:600;color:var(--accent);font-size:11.5px;line-height:1.45;margin-bottom:10px}
.focus .body-text{font-size:10.4px}
.areas{position:relative;height:170px;margin:8px -26px 12px;background:linear-gradient(135deg,#4a5b60,#22323a 60%,#1a262c)}
.areas__text{position:absolute;right:22px;top:24px;text-align:right;color:#fff;font-family:"Raleway",sans-serif}
.areas__head{font-weight:700;font-size:15px;margin-bottom:6px}
.areas__item{font-weight:300;font-size:14px;line-height:1.55;letter-spacing:.5px}
.skills__title{font-weight:700;color:var(--teal-dark);font-size:15px;margin-bottom:6px}
.bullet-list{list-style:none}
.bullet-list li{position:relative;padding-left:14px;font-size:12px;line-height:1.55}
.bullet-list li::before{content:"";position:absolute;left:0;top:7px;width:5px;height:5px;border-radius:50%;background:var(--ink)}
.room-photo{position:absolute;right:20px;bottom:58px;width:120px;height:90px;background:linear-gradient(160deg,#f1ece4,#c9bba8)}

/* inside middle */
.services{background:linear-gradient(180deg,#4a8a96,#2f6571 55%);height:470px;padding:28px 26px;color:#e8f1f3}
.services__title{font-family:"Raleway",sans-serif;font-weight:600;color:var(--sky);font-size:20px;margin-bottom:10px}
.services__sub{font-family:"Raleway",sans-serif;font-weight:600;color:#fff;font-size:15px;margin-bottom:4px}
.services__intro{font-style:italic;color:var(--sky);font-size:10.5px;line-height:1.45;margin-bottom:10px}
.services .body-text,.adolescent .body-text{color:#dce8eb}
.adolescent{background:var(--navy);height:411px;padding:28px 26px;color:#e8f1f3}

/* inside right */
.specialties{background:linear-gradient(180deg,#3c7884,#26525d);height:450px;padding:30px 30px;color:#eef5f6}
.specialties__title{font-weight:700;font-size:14px;margin-bottom:8px}
.specialties .bullet-list li{font-size:11px;line-height:1.6}
.specialties .bullet-list li::before{background:#eef5f6}
.couples{padding:24px 30px}
.couples__title{font-weight:700;font-size:15px;color:var(--teal-dark);margin-bottom:6px}
.couples__intro{font-style:italic;font-weight:600;color:var(--accent);font-size:10.5px;line-height:1.45;margin-bottom:10px}
.couples .bullet-list li{font-size:10.5px}
</style>
</head>
<body>

<section class="spread spread--outside">
  <article class="panel approach">
    <h3 class="heading-teal">My approach:</h3>
    <p class="body-text">As a clinical psychologist, I deliver a treatment approach that is genuine, direct, and effective. My treatment approach is tailored to each client and typically involves a blend of evidence-based treatments including Cognitive Behavioral Therapy, Dialectical Behavior Therapy, Imagery Rehearsal Therapy and Interpersonal Psychotherapy. Together we work to uncover and better understand day-to-day stressors that detract from your life and sense of wellbeing, identifying and practicing skills that will improve your overall quality of life.</p>
    <h3 class="heading-teal">Cognitive Behavioral Therapy (CBT)</h3>
    <p class="body-text">Cognitive Behavioral Therapy is an empirically based, short-term therapy which focuses on the collaborative relationship between therapist and client. Treatment is designed to help the client understand the relationship between thoughts, feelings and behaviors and learn how to reframe unhelpful thinking patterns. Through skill building and cognitive restructuring, CBT promotes long-term results that can improve your overall quality of life.</p>
    <h3 class="heading-teal">Dialectical Behavior Therapy (DBT)</h3>
    <p class="body-text">Dialectical Behavior Therapy is an evidence-based, cognitive behavioral treatment which focuses on accepting clients as they are while also acknowledging the need to change in order to reach their goals. A key component of DBT is skills training, which includes mindfulness, distress tolerance, emotion regulation and interpersonal effectiveness. Though DBT was initially developed for borderline personality disorder, research demonstrates its efficacy for many disorders including depression and anxiety.</p>
    <h3 class="heading-teal">Imagery Rehearsal Therapy (IRT)</h3>
    <p class="body-text">Imagery Rehearsal Therapy is a behavioral treatment for reducing the number and intensity of nightmares among people with posttraumatic stress disorder. The treatment has been modified to treat nightmares and flashbacks experienced by survivors of physical or sexual trauma. IRT is a short-term and does not require clients to relive the traumatic event or prolonged exposure therapy.</p>
    <h2 class="heading-dark">Getting Started:</h2>
    <h3 class="heading-sub">Consultation</h3>
    <p class="body-text">I offer a complimentary 30-minute consultation (on the phone), so you can get a sense of whether we are a good fit. It will also give me an opportunity to determine if I am the best therapist to be able to help you. In the event that we are not a good match, I can connect you with another practitioner to better meet your needs.</p>
    <h3 class="heading-sub">Intake</h3>
    <p class="body-text">During our first session, we will address your presenting problem(s) and collect a thorough background of your history, so that I can best understand your problem areas in the context of who you are. We will also conduct an assessment of your current symptoms, address provisional diagnoses.</p>
  </article>

  <article class="panel">
    <div class="bio">
      <div class="bio__portrait" role="img" aria-label="Portrait photograph of the psychologist"></div>
      <h3 class="bio__title">Bio-</h3>
      <p class="body-text">Dr. Marlow graduated from the Coastal State University and received her Doctoral degree in Clinical Psychology at the Western School of Professional Psychology. She completed her predoctoral internship in behavioral medicine and rehabilitation psychology at the Northfield Veterans Healthcare System, Kestrel Valley Medical School and a postdoctoral fellowship at the Cognitive Intensive Outpatient Program, Bayside Vista Hospital.</p>
      <p class="body-text">Dr. Marlow is a member of the National Psychological Society, Guild of Cognitive Therapy, and the Harbor County Psychological Association.</p>
    </div>
    <div class="contact">
      <p class="contact__lead">By Appointment Only</p>
      <p class="contact__lines">Elena Marlow, Psy.D<br>418 Linden Avenue<br>Suite 210<br>Bayview, CA 90000</p>
      <p class="contact__phone">555 014 2290</p>
      <p class="contact__email">emarlow@harborpointpsych.com</p>
    </div>
    <div class="map" role="img" aria-label="Street map showing the office location"></div>
  </article>

  <article class="panel cover">
    <div class="cover__brand">
      <span class="brand-dot"></span>
      <span class="brand-name">Harbor Point<br>Psychological<br>Services</span>
    </div>
    <div class="cover__photo" role="img" aria-label="Photograph of a head silhouette in profile filled with a sunset over water"></div>
    <div class="cover__tagline">Personalized<br>Solutions<br>| Positive Change</div>
  </article>
</section>

<section class="spread spread--inside">
  <article class="panel focus">
    <h2 class="focus__title">Treatment Focus</h2>
    <p class="focus__intro">I pride myself on being more than just someone to listen, but someone who takes a hands-on, practical approach to problem-solving.</p>
    <p class="body-text">It's important to face the challenges of life head-on, but with the right skills and tools in your toolbox. I aim to build a collaborative relationship with you and assist you in understanding the relationship between negative thought patterns and ineffective coping strategies.</p>
    <p class="body-text">We work together to develop a healthier thought process and effective coping skills, ultimately decreasing symptoms and improving your overall quality of life.</p>
    <div class="areas" role="img" aria-label="Photograph of a magnifying glass on a wooden desk">
      <div class="areas__text">
        <p class="areas__head">MY AREAS OF FOCUS INCLUDE:</p>
        <p class="areas__item">ADULT THERAPY</p>
        <p class="areas__item">ADOLESCENT THERAPY</p>
        <p class="areas__item">COUPLES THERAPY</p>
      </div>
    </div>
    <h3 class="skills__title">Typical Skills Developed in Treatment:</h3>
    <ul class="bullet-list">
      <li>Cognitive Restructuring</li>
      <li>Decatastrophizing</li>
      <li>Distress Tolerance</li>
      <li>Emotion Regulation</li>
      <li>Healthy Grieving of Losses</li>
      <li>Healthy Personal Boundaries</li>
      <li>Interpersonal Effectiveness</li>
      <li>Imagery Techniques</li>
      <li>Mindfulness</li>
      <li>Problem Solving</li>
      <li>Stress Management</li>
    </ul>
    <div class="room-photo" role="img" aria-label="Photograph of a calm office interior with a sofa"></div>
  </article>

  <article class="panel">
    <div class="services">
      <h2 class="services__title">Services:</h2>
      <h3 class="services__sub">Adult Therapy:</h3>
      <p class="services__intro">Adult life consists of alternating periods of stability and transition.</p>
      <p class="body-text">Whatever the circumstance, navigating life transitions can be difficult, resulting in new ways of thinking and feeling that can be overwhelming. Adults may demonstrate difficult responses to address these challenges, and a therapist can help in managing mental health concerns such as depression, anxiety and relationship stress. Whatever the reason, therapy can assist you in finding your footing, and learn how to cope with your situation in a different way.</p>
      <p class="body-text">Treatment begins by building rapport and forming a collaborative therapeutic relationship with my clients. While many clients benefit after 12 to 16 sessions of structured work, the length of treatment is determined collaboratively and depends on the nature of the presenting problems, personality, and level of support.</p>
    </div>
    <div class="adolescent">
      <h3 class="services__sub">Adolescent Therapy:</h3>
      <p class="services__intro">Adolescence is a period of time involving multiple physical, intellectual, personality, and social developmental changes.</p>
      <p class="body-text">There is a process of developing the social skills and emotional intelligence necessary to lead healthy, happy lives. When adolescents experience difficult emotions or engage in behaviors that interfere with their happiness and ability to thrive, they may benefit from engaging in therapy to address their problems.</p>
      <p class="body-text">Treatment is not a one size fits all approach and careful consideration is taken to understand the unique issues that each adolescent faces. I spend time building rapport with your teen to foster open communication and trust in the relationship, thus promoting motivation and openness to suggestions and strategies for change. I also work with the parents to foster empowerment in their ability to learn more effective skills to support their child.</p>
    </div>
  </article>

  <article class="panel">
    <div class="specialties">
      <h3 class="specialties__title">Specialties &amp; Issues:</h3>
      <ul class="bullet-list">
        <li>Anger Management</li>
        <li>Anxiety</li>
        <li>Borderline Personality Disorder</li>
        <li>Chronic Illness / Pain</li>
        <li>Coping Skills</li>
        <li>Depression</li>
        <li>Disruptive Behaviors</li>
        <li>Grief / Loss</li>
        <li>Life Adjustments / Transitions</li>
        <li>Mood Disorders</li>
        <li>Panic Disorder</li>
        <li>Problems with Interpersonal Relationships</li>
        <li>Post-Traumatic Stress Disorder</li>
        <li>Sleep Disorders</li>
        <li>Stress Management</li>
      </ul>
    </div>
    <div class="couples">
      <h3 class="couples__title">Couples Therapy:</h3>
      <p class="couples__intro">Many couples struggle with communicating effectively and feeling that they are heard by their partner, as well as differences in expectations or belief systems.</p>
      <p class="body-text">Issues can also be rooted in a relationship that simply grows apart over time, or trust that has been broken. Couples therapy offers a safe space to explore these concerns and work toward repair.</p>
      <p class="body-text">Treatment is designed to be present focused and goal oriented, helping partners improve communication, rebuild trust, and resolve conflict in healthier ways. Together we identify patterns that keep you stuck and practice new skills to strengthen your connection.</p>
      <h3 class="heading-sub">Couples Specialties &amp; Issues:</h3>
      <ul class="bullet-list">
        <li>Communication Issues</li>
        <li>Conflict Resolution</li>
        <li>Family Dysfunction</li>
        <li>Infidelity / Trust</li>
      </ul>
    </div>
  </article>
</section>

</body>
</html>
```